Salon and Spa Distributor Business Card

Need a business card. We are are distributor in the salon and spa industry. We identify with natural beauty. Need a card with:
Company Name: Petal Haven"
Title: "President & CEO"
Address
Company Phone number
email
website
Tag Line:" The Professional Salon Source"

Industry/Entity Type

Business

Contact Information for Business Card

Name: Lena Morcott
Title: "President & CEO"
Address: 317 Birchfield Ln, Oakvane, NJ 07481
Company Phone number: 800-463-9152
email: lenamorcott@petalhaven-example.com
website: www.petalhaven-example.com

Requirements
Should not have
• No black backgrounds

```html
<!DOCTYPE html>
<html lang="en">
<head>
<meta charset="utf-8">
<title>Petal Haven — Business Card</title>
<link rel="stylesheet" href="https://fonts.googleapis.com/css2?family=Nunito+Sans:wght@400;600;700&display=swap">
<style>
  :root {
    --leaf-green: #65b32e;
    --forest-green: #24733a;
    --paper: #ffffff;
    --backdrop: #e9eaea;
    --ink-light: #ffffff;
    --shadow: rgba(0, 0, 0, 0.18);
  }
  * { box-sizing: border-box; margin: 0; padding: 0; }
  html, body {
    width: 1200px;
    height: 863px;
    overflow: hidden;
    background: var(--backdrop);
    font-family: "Nunito Sans", Arial, sans-serif;
  }
  .stage {
    position: relative;
    width: 1200px;
    height: 863px;
    display: flex;
    justify-content: center;
    align-items: center;
    gap: 60px;
  }
  .card {
    position: relative;
    width: 300px;
    height: 525px;
    overflow: hidden;
    box-shadow: 0 10px 28px var(--shadow);
  }
  .card__shapes {
    position: absolute;
    inset: 0;
    width: 100%;
    height: 100%;
  }
  .brand {
    position: absolute;
    display: flex;
    align-items: center;
    gap: 10px;
    color: var(--leaf-green);
    font-weight: 600;
    white-space: nowrap;
  }
  .brand__dot {
    width: 34px;
    height: 34px;
    border-radius: 50%;
    background: var(--leaf-green);
    flex: none;
  }
  .card--front .brand {
    left: 40px;
    top: 246px;
    font-size: 28px;
  }
  .card--back .brand {
    left: 50px;
    top: 92px;
    font-size: 28px;
  }
  .contact {
    position: absolute;
    left: 0;
    right: 0;
    color: var(--ink-light);
  }
  .contact__name {
    position: absolute;
    top: 292px;
    right: 26px;
    font-size: 30px;
    font-weight: 600;
    line-height: 1;
  }
  .contact__title {
    position: absolute;
    top: 326px;
    right: 80px;
    font-size: 13px;
    font-weight: 400;
  }
  .contact__row {
    position: absolute;
    left: 22px;
    display: flex;
    align-items: flex-start;
    gap: 12px;
    font-size: 12.5px;
    line-height: 1.35;
  }
  .contact__row--phone { top: 350px; }
  .contact__row--web { top: 394px; }
  .contact__icon {
    width: 14px;
    height: 14px;
    flex: none;
    margin-top: 1px;
  }
  .contact__address {
    position: absolute;
    left: 22px;
    top: 480px;
    font-size: 13.5px;
    font-weight: 600;
    color: var(--ink-light);
  }
</style>
</head>
<body>
<main class="stage">

  <section class="card card--front" aria-label="Business card front">
    <svg class="card__shapes" viewBox="0 0 300 525" aria-hidden="true">
      <rect width="300" height="525" fill="var(--leaf-green)"/>
      <ellipse cx="155" cy="262" rx="192" ry="150" fill="var(--forest-green)"/>
      <ellipse cx="148" cy="268" rx="178" ry="136" fill="var(--paper)"/>
    </svg>
    <div class="brand"><span class="brand__dot"></span>Petal Haven</div>
  </section>

  <section class="card card--back" aria-label="Business card back">
    <svg class="card__shapes" viewBox="0 0 300 525" aria-hidden="true">
      <rect width="300" height="525" fill="var(--paper)"/>
      <path d="M0 236 Q150 320 300 236 L300 525 L0 525 Z" fill="var(--leaf-green)"/>
      <path d="M0 258 Q150 300 300 262 L300 445 L0 445 Z" fill="var(--forest-green)"/>
    </svg>

    <div class="brand"><span class="brand__dot"></span>Petal Haven</div>

    <div class="contact">
      <p class="contact__name">Lena Morcott</p>
      <p class="contact__title">President &amp; CEO</p>

      <p class="contact__row contact__row--phone">
        <svg class="contact__icon" viewBox="0 0 24 24" aria-hidden="true">
          <path fill="#fff" d="M6.6 10.8a15.1 15.1 0 0 0 6.6 6.6l2.2-2.2a1 1 0 0 1 1-.25 11.4 11.4 0 0 0 3.6.57 1 1 0 0 1 1 1V20a1 1 0 0 1-1 1A17 17 0 0 1 3 4a1 1 0 0 1 1-1h3.5a1 1 0 0 1 1 1c0 1.25.2 2.45.57 3.57a1 1 0 0 1-.25 1z"/>
        </svg>
        <span>800-463-9152</span>
      </p>

      <p class="contact__row contact__row--web">
        <svg class="contact__icon" viewBox="0 0 24 24" aria-hidden="true">
          <g fill="none" stroke="#fff" stroke-width="1.8">
            <circle cx="12" cy="12" r="9.5"/>
            <ellipse cx="12" cy="12" rx="4.2" ry="9.5"/>
            <line x1="2.5" y1="12" x2="21.5" y2="12"/>
          </g>
        </svg>
        <span>lenamorcott@petalhaven-example.com<br>www.petalhaven-example.com</span>
      </p>
    </div>

    <p class="contact__address">317 Birchfield Ln, Oakvane, NJ 07481</p>
  </section>

</main>
</body>
</html>
```